Harlow Creekside Clinic Tri-Fold Flyer

a marketing 3- fold flyer for primary business awareness. this should offer all aspects of our medical practice. I have provided several pictures as well as all pertinent information needed to make a successful flyer. This needs to be eye catching and attractive. each page should feature something of its own.
my thoughts:
page 1- photo of office our mission statement and maybe our phone number and address
page 2- our HCC A-team flyer
page 3- our paragraph on our practice as well as some of our services. say something like we offer a wide scope of services including health coaching, weight loss. A "patient services coordinator" will help you pick out what services we can do for you. a pic
page 4- doctors bio and pics and logos
page 5-
page 6- our map our address and phone numbers. the sentence on making an appointment. our web page and facebook as well as our logos

Target Market(s)

we are a medical practice, so we are seeking new patients

Industry/Entity Type

Health Care

Font styles to use
Serif

Colors
34a6d7
33b8a4
abd036
fbee3e

Requirements
Must have
• I have enclosed a tri-fold info attachment as well as other pieces. Use what you feel will make our flyer attractive. Not too busy. Please try to get most info in
• All work purchased should be delivered with the PDF form for future changes by owner of medical office.
Nice to have
• All Info provided

```html
<!DOCTYPE html>
<html lang="en">
<head>
<meta charset="utf-8">
<title>Harlow Creekside Clinic Tri-Fold Flyer</title>
<link href="https://fonts.googleapis.com/css2?family=Lato:wght@300;400;700&display=swap" rel="stylesheet">
<style>
  :root {
    --backdrop: #c9ced4;
    --blue: #37a6d9;
    --teal-dark: #1d8c79;
    --teal: #1aa392;
    --banner: #11a078;
    --ink: #1c1c1c;
    --white: #ffffff;
    --logo: #2a6f9e;
  }
  * { margin: 0; padding: 0; box-sizing: border-box; }
  html, body { width: 1200px; height: 870px; overflow: hidden; background: var(--backdrop); }
  body { font-family: "Lato", sans-serif; position: relative; }

  .spread { position: absolute; left: 102px; top: 47px; width: 998px; height: 774px; overflow: hidden; background: var(--white); }

  .panel-left { position: absolute; left: 0; top: 0; width: 331px; height: 774px; background: var(--blue); }
  .office-photo { position: absolute; left: 0; top: 0; width: 331px; height: 297px;
    background: linear-gradient(180deg, #8fb4dc 0%, #b9cde0 35%, #7a5a48 55%, #55585c 75%, #6d6f72 100%); }
  .strip-dark { position: absolute; left: 0; top: 297px; width: 331px; height: 25px; background: var(--teal-dark); }
  .strip-teal { position: absolute; left: 0; top: 322px; width: 331px; height: 23px; background: var(--teal); }
  .about { position: absolute; left: 44px; top: 390px; width: 250px; color: var(--white); font-size: 12.2px; line-height: 17.4px; font-weight: 400; }
  .insurance { position: absolute; left: 44px; top: 648px; color: var(--white); font-size: 14.5px; font-weight: 700; }

  .cover-photo { position: absolute; left: 331px; top: 0; width: 667px; height: 774px;
    background: linear-gradient(180deg, #9fcdee 0%, #d6e9f5 35%, #e7f1ef 55%, #b9d77a 68%, #9cc63a 85%, #a6cb2e 100%); }

  .brand { position: absolute; display: flex; align-items: center; gap: 7px; color: var(--logo); font-weight: 400; letter-spacing: 0.3px; white-space: nowrap; }
  .brand-dot { width: 26px; height: 26px; border-radius: 50%; background: var(--blue); flex: none; }
  .brand-name { font-size: 14px; line-height: 1; }
  .brand-top { right: 36px; top: 66px; }
  .brand-bottom { left: 378px; top: 608px; }

  .banner { position: absolute; left: 660px; top: 463px; width: 338px; height: 95px; background: var(--banner); color: var(--white); text-align: right; padding-right: 50px; }
  .banner-light { display: block; font-size: 31px; font-weight: 300; padding-top: 16px; line-height: 30px; }
  .banner-bold { display: block; font-size: 32px; font-weight: 700; line-height: 34px; }

  .contact { position: absolute; left: 384px; top: 656px; color: var(--ink); font-size: 12px; line-height: 15.2px; }
  .contact p + p { margin-top: 14px; }

  .call { position: absolute; left: 748px; top: 700px; color: var(--ink); }
  .call-line { font-size: 12px; }
  .call-number { font-size: 32px; font-weight: 400; line-height: 32px; }
</style>
</head>
<body>
  <main class="spread">
    <section class="panel-left">
      <div class="office-photo" role="img" aria-label="Photo of the clinic building and parking lot under a blue sky"></div>
      <div class="strip-dark"></div>
      <div class="strip-teal"></div>
      <p class="about">Our physicians serving Maple Ridge and the surrounding area. Our doctors and the rest of the welcoming team at Harlow Creekside Clinic, LLC are committed to providing integrative medical solutions to address your unique needs, whether you are experiencing back pain, knee pain, or even muscular tightness and tension. You may be searching for pain relief after an accident, experiencing an injury, or if you suffer from a specific condition like chronic back pain or knee pain. Even if you looking to improve your overall health &amp; nutrition, our doctor can help you attain your everyday wellness goals!</p>
      <p class="insurance">We accept most major insurances</p>
    </section>

    <div class="cover-photo" role="img" aria-label="Photo of a smiling family in a sunny green field, a child riding on a man's shoulders"></div>

    <div class="brand brand-top"><span class="brand-dot"></span><span class="brand-name">Harlow Creekside Clinic</span></div>

    <div class="banner">
      <span class="banner-light">We Create</span>
      <span class="banner-bold">Healthy People</span>
    </div>

    <div class="brand brand-bottom"><span class="brand-dot"></span><span class="brand-name">Harlow Creekside Clinic</span></div>

    <div class="contact">
      <p>Harlow Creekside Clinic, LLC<br>48 Larkspur Way Suite 210 Maple<br>Ridge, VA 20111</p>
      <p>Phone: 555-014-2270<br>Fax: 555-014-2271</p>
    </div>

    <div class="call">
      <p class="call-line">Call today to make an appointment.</p>
      <p class="call-number">555-014-2270</p>
    </div>
  </main>
</body>
</html>
```